Electronic Letterhead for The Harborline Partners, LLC

I would like to have an electronic letterhead layout using Word for first and second page letterhead using my previously designed logo. The logo was successfully designed by a designer for the Pixel Bazaar. I would like to only use the "C" portion of the logo on the second page. I would like the designer that designed my logo to be included in the designers that participate in this competition.

Target Market(s)

My clients are typically governmental entities or financial entities

Industry/Entity Type

Electronic

Font styles to use
Sans Serif

Requirements
Must have
• Utilize existing logo
Nice to have
• Fist and second page letterhead design in electronic format (Word)

```html
<!DOCTYPE html>
<html lang="en">
<head>
<meta charset="utf-8">
<title>The Harborline Partners, LLC – Letterhead Pages</title>
<link rel="stylesheet" href="https://fonts.googleapis.com/css2?family=Carlito:wght@400;700&family=Tinos:wght@700&display=swap">
<style>
  :root {
    --backdrop: #dedede;
    --paper: #ffffff;
    --navy: #2e3f7c;
    --ink: #1c1c1c;
    --rule: #9a9a9a;
    --soft-mark: #d9deea;
  }
  * { box-sizing: border-box; margin: 0; padding: 0; }
  html, body { width: 1200px; height: 921px; overflow: hidden; }
  body {
    background: var(--backdrop);
    font-family: "Carlito", "Calibri", sans-serif;
    color: var(--ink);
    position: relative;
  }
  .page {
    position: absolute;
    background: var(--paper);
    box-shadow: 0 4px 14px rgba(0,0,0,.25);
    overflow: hidden;
  }
  .page--first { left: 28px; top: 68px; width: 582px; height: 760px; }
  .page--continuation { left: 615px; top: 128px; width: 560px; height: 722px; }

  .brand {
    position: absolute;
    display: flex;
    align-items: center;
    gap: 10px;
  }
  .page--first .brand { left: 27px; top: 38px; }
  .page--continuation .brand { left: 35px; top: 36px; }
  .brand__dot {
    width: 62px; height: 62px;
    border-radius: 50%;
    background: var(--navy);
    flex: none;
  }
  .brand__divider {
    width: 1px; height: 82px;
    background: var(--rule);
    flex: none;
  }
  .brand__name {
    font-size: 22px;
    line-height: 1.15;
    color: var(--navy);
    font-weight: 400;
    letter-spacing: .5px;
    text-transform: uppercase;
  }
  .header-rule {
    position: absolute;
    left: 0; right: 0;
    height: 1px;
    background: var(--rule);
  }
  .page--first .header-rule { top: 115px; }
  .page--continuation .header-rule { top: 117px; }

  .letter {
    position: absolute;
    left: 82px;
    width: 432px;
    font-size: 10.6px;
    line-height: 1.42;
  }
  .letter p { margin-bottom: 11px; text-align: justify; }
  .letter .letter__date { margin-bottom: 14px; }
  .letter address { font-style: normal; margin-bottom: 14px; }
  .letter .letter__closing { margin-top: 20px; margin-bottom: 68px; }

  .footer-rule {
    position: absolute;
    left: 18px; right: 0; top: 664px;
    height: 1px; background: var(--rule);
  }
  .footer-contact {
    position: absolute;
    left: 0; right: 0; top: 672px;
    text-align: center;
    font-family: "Tinos", "Times New Roman", serif;
    font-weight: 700;
    font-size: 13px;
    line-height: 1.5;
  }

  .legend {
    position: absolute;
    left: 100px; top: 120px;
    width: 396px;
    font-size: 10px;
    line-height: 1.4;
  }
  .legend__title { margin-bottom: 10px; }
  .legend ul { padding-left: 20px; margin-bottom: 12px; }
  .legend li { margin-bottom: 5px; text-align: justify; }
  .legend p { margin-bottom: 14px; }
  .legend .legend__thanks { text-align: center; margin-top: 4px; }

  .bottom-rule {
    position: absolute;
    left: 0; top: 652px; width: 390px;
    height: 1px; background: var(--rule);
  }
  .corner-mark {
    position: absolute;
    left: 390px; top: 588px;
  }
</style>
</head>
<body>

<section class="page page--first" aria-label="First page letterhead">
  <header class="brand">
    <span class="brand__dot"></span>
    <span class="brand__divider"></span>
    <span class="brand__name">The Harborline<br>Partners, LLC</span>
  </header>
  <div class="header-rule"></div>

  <article class="letter" style="top:132px">
    <p class="letter__date">Date: June 10, 2014</p>
    <address>The Company<br>480 Maple Crest Way<br>Lakeview, FL 32801</address>
    <p>Dear Customer,</p>
    <p>We recently purchased one of your xxxxx (Model # 12345) for my three-year old. Unfortunately, the components that came with the product, I discovered that four of the parts. Also, the instructions that came with the tent are incomplete. Both of these situations have resulted in the tent remaining unassembled and unacceptable as a part.</p>
    <p>We are writing to request replacements for the missing parts, and a copy of the full set of assembly directions for the model I purchased. If reasonable arrangements are not made within ten business days, I will return the tent to the store I purchased it from and expect a full refund. To assist you in processing my request, I am including a copy of my sales receipt and a list of the missing parts.</p>
    <p>We are writing to request replacements for the missing parts, and a copy of the full set of assembly directions for the model I purchased. If reasonable arrangements are not made within ten business days, I will return the tent to the store I purchased it from and expect a full refund. To assist you in processing my request, I am including a copy of my sales receipt and a list of the missing parts.</p>
    <p>We have purchased other toys manufactured by your company in the past, and have always been impressed with the quality and selection Little Sprouts has made available to its customers. I sincerely hope this is a one-time incident, and that any future purchases I make will live up to the standard my family has come to expect from your company.</p>
    <p class="letter__closing">Sincerely,</p>
    <p>Enclosures:</p>
  </article>

  <div class="footer-rule"></div>
  <footer class="footer-contact">
    Address : # , Street Name, City, State Zip code<br>
    Phone: 555-014-2297<br>
    E-Mail : office@harborlinepartners.com
  </footer>
</section>

<section class="page page--continuation" aria-label="Continuation page letterhead">
  <header class="brand">
    <span class="brand__dot"></span>
    <span class="brand__divider"></span>
    <span class="brand__name">The Harborline<br>Partners, LLC</span>
  </header>
  <div class="header-rule"></div>

  <div class="legend">
    <p class="legend__title">Legend:</p>
    <ul>
      <li>Replace the text in brackets [ ] with the component indicated. Don't type the brackets.</li>
      <li>Try to keep your letters to one page, but see page 2 of this sample if you need continuation pages.</li>
      <li>How many blank lines you add between lines that require more than one, depends on how much space is available on the page.</li>
      <li>The same goes for margins. One and one-half inch (108 points) for short letters and one inch (72 points) for longer letters are standard. If there is a letterhead, its position determines the top margin on page 1.</li>
      <li>If you don't type one of the more formal components, don't leave space for them.</li>
    </ul>
    <p>For example, if you don't type the Reference Line (3), Special Mailing. For example, if you don't type the Reference Line (3), Special Mailing For example, if you don't type the Reference Line (3), Special Mailing</p>
    <p>For example, if you don't type the Reference Line (3), Special Mailing. For example, if you don't type the Reference Line (3), Special Mailing For example, if you don't type the Reference Line (3), Special Mailing</p>
    <p>For example, if you don't type the Reference Line (3), Special Mailing. For example, if you don't type the Reference Line (3), Special Mailing For example, if you don't type the Reference Line (3), Special Mailing</p>
    <p>For example, if you don't type the Reference Line (3), Special Mailing. For example, if you don't type the Reference Line (3), Special Mailing For example, if you don't type the Reference Line (3), Special Mailing</p>
    <p class="legend__thanks">Thanks</p>
  </div>

  <div class="bottom-rule"></div>
  <svg class="corner-mark" width="160" height="160" viewBox="0 0 160 160" aria-hidden="true">
    <circle cx="80" cy="80" r="74" fill="var(--soft-mark)"/>
  </svg>
</section>

</body>
</html>
```